Refresh of The Marston Collective business card

Update business card design using existing primary logo. Names, numbers, etc. are too hard to read on current design.

Target Market(s)

We are a CPA firm.

Industry/Entity Type

Accountant

Contact Information for Business Card

update current card

Colors
0355a3
3176b5
85acd3
0792cd

Requirements
Must have
• Easier to read phone numbers and names
• Use existing logo
Nice to have
• We love our color scheme and current TMC logo. But the names and phone numbers are too small and card just look old and stale.

```html
<!DOCTYPE html>
<html lang="en">
<head>
<meta charset="utf-8">
<title>The Marston Collective – Business Card</title>
<link rel="stylesheet" href="https://fonts.googleapis.com/css2?family=Cinzel:wght@600&family=Questrial&display=swap">
<style>
  :root {
    --navy: #0b2a5c;
    --navy-deep: #0a1e45;
    --brand-blue: #0355a3;
    --mid-blue: #3176b5;
    --light-blue: #85acd3;
    --bright-blue: #0792cd;
    --charcoal: #3b3d42;
    --ink: #2f3440;
    --rule: #b9bec7;
    --paper: #ffffff;
    --backdrop: #e6e7ea;
  }
  * { box-sizing: border-box; margin: 0; padding: 0; }
  html, body {
    width: 1200px; height: 900px; overflow: hidden;
    background: var(--backdrop);
  }
  .canvas { position: relative; width: 1200px; height: 900px; }

  .card {
    position: absolute; width: 560px; height: 320px;
    box-shadow: 0 10px 24px rgba(0,0,0,.18);
    overflow: hidden;
  }

  /* Back of card */
  .card-back {
    left: 80px; top: 110px;
    background: radial-gradient(ellipse at 45% 40%, var(--brand-blue) 0%, #0a3f80 45%, var(--navy-deep) 100%);
    color: var(--paper);
  }
  .card-back .map-texture {
    position: absolute; inset: 30px 40px 70px 40px;
    background: radial-gradient(ellipse at center, rgba(133,172,211,.18), rgba(133,172,211,0) 70%);
  }
  .card-back .lockup {
    position: absolute; left: 110px; top: 110px;
    display: flex; align-items: center; gap: 18px;
  }
  .card-back .lockup-mark {
    width: 96px; height: 96px; border-radius: 50%;
    background: var(--paper); border: 3px solid var(--light-blue);
  }
  .card-back .lockup-text { width: 240px; }
  .card-back .lockup-name { color: var(--paper); border-color: rgba(255,255,255,.7); }
  .card-back .lockup-tagline { color: var(--paper); }
  .card-back .website {
    position: absolute; left: 0; right: 0; bottom: 34px;
    text-align: center;
    font-family: "Questrial", sans-serif; font-size: 17px; letter-spacing: .5px;
  }

  /* Shared lockup type */
  .lockup-text { display: flex; flex-direction: column; }
  .lockup-name {
    font-family: "Cinzel", serif; font-weight: 600;
    font-size: 26px; line-height: 1.1;
    border-top: 1px solid; border-bottom: 1px solid;
    padding: 6px 0 6px;
  }
  .lockup-tagline {
    margin-top: 6px;
    font-family: "Questrial", sans-serif; font-size: 8.5px; letter-spacing: 2px;
    text-transform: uppercase; white-space: nowrap;
  }

  /* Front of card */
  .card-front { left: 560px; top: 470px; background: var(--paper); }
  .card-front .lockup {
    position: absolute; left: 24px; top: 84px;
    display: flex; align-items: center; gap: 12px;
  }
  .card-front .lockup-mark {
    width: 78px; height: 78px; border-radius: 50%; flex: none;
    background: radial-gradient(circle at 40% 35%, var(--mid-blue), var(--navy));
    border: 3px solid var(--navy-deep);
  }
  .card-front .lockup-text { width: 160px; }
  .card-front .lockup-name { color: var(--navy); font-size: 17px; border-color: var(--navy); padding: 5px 0; }
  .card-front .lockup-tagline { color: var(--navy); font-size: 6px; letter-spacing: 1px; }

  .divider {
    position: absolute; left: 296px; top: 28px; width: 1px; height: 180px;
    background: var(--rule);
  }
  .contact {
    position: absolute; left: 312px; top: 34px;
    font-family: "Questrial", sans-serif; color: var(--ink);
  }
  .contact-name {
    font-family: "Cinzel", serif; font-weight: 600;
    font-size: 16px; color: var(--navy); margin-bottom: 6px; white-space: nowrap;
  }
  .contact-name .credential { color: var(--brand-blue); }
  .contact-address { font-size: 13px; line-height: 1.3; margin-bottom: 10px; }
  .contact-list { list-style: none; font-size: 13px; line-height: 1.35; }
  .contact-list li { display: flex; align-items: center; gap: 6px; }
  .contact-icon { width: 12px; height: 12px; flex: none; }

  .card-front .footer-bands { position: absolute; left: 0; bottom: 0; width: 560px; height: 320px; }
</style>
</head>
<body>
<div class="canvas">

  <section class="card card-back" aria-label="Card back">
    <div class="map-texture" role="img" aria-label="Faint dotted world map texture"></div>
    <div class="lockup">
      <div class="lockup-mark"></div>
      <div class="lockup-text">
        <span class="lockup-name">The Marston Collective</span>
        <span class="lockup-tagline">Certified Public Accountants</span>
      </div>
    </div>
    <p class="website">www.marstoncollective.com</p>
  </section>

  <section class="card card-front" aria-label="Card front">
    <svg class="footer-bands" viewBox="0 0 560 320" aria-hidden="true">
      <defs>
        <linearGradient id="band-blue" x1="0" y1="0" x2="1" y2="0">
          <stop offset="0" stop-color="#0a1e45"/>
          <stop offset="0.6" stop-color="#0355a3"/>
          <stop offset="1" stop-color="#3176b5"/>
        </linearGradient>
      </defs>
      <polygon points="380,258 560,238 560,262 392,272" fill="#3b3d42"/>
      <polygon points="0,320 0,292 300,278 380,272 395,268 560,262 560,320" fill="url(#band-blue)"/>
    </svg>

    <div class="lockup">
      <div class="lockup-mark"></div>
      <div class="lockup-text">
        <span class="lockup-name">The Marston Collective</span>
        <span class="lockup-tagline">Certified Public Accountants</span>
      </div>
    </div>

    <div class="divider"></div>

    <div class="contact">
      <h1 class="contact-name">Daniel R. Marston, <span class="credential">CPA</span></h1>
      <p class="contact-address">The Marston Collective<br>318 Lakeview Ave. Suite 104<br>Winter Park, Florida 32789</p>
      <ul class="contact-list">
        <li>
          <svg class="contact-icon" viewBox="0 0 12 12"><circle cx="6" cy="6" r="6" fill="#0355a3"/><path d="M4 3.2l1 1.3-.6.7a4 4 0 0 0 2.4 2.4l.7-.6 1.3 1-.6 1C6 9 3 6 3 3.8z" fill="#fff"/></svg>
          407.555.0142
        </li>
        <li>
          <svg class="contact-icon" viewBox="0 0 12 12"><circle cx="6" cy="6" r="6" fill="#0355a3"/><rect x="3" y="4" width="6" height="4.5" rx=".6" fill="#fff"/><rect x="4" y="2.8" width="4" height="1.6" fill="#fff"/></svg>
          407.555.0187
        </li>
        <li>
          <svg class="contact-icon" viewBox="0 0 12 12"><circle cx="6" cy="6" r="6" fill="#0355a3"/><rect x="4.2" y="2.6" width="3.6" height="6.8" rx=".6" fill="#fff"/></svg>
          407.555.0193
        </li>
        <li>
          <svg class="contact-icon" viewBox="0 0 12 12"><circle cx="6" cy="6" r="6" fill="#0355a3"/><rect x="3" y="4" width="6" height="4" fill="#fff"/><path d="M3 4l3 2.2L9 4" fill="none" stroke="#0355a3" stroke-width=".7"/></svg>
          dan@marstoncollective.com
        </li>
      </ul>
    </div>
  </section>

</div>
</body>
</html>
```